Retiros Silencio

I want a Catholic flyer, with the Virgen Mary showing aiding, praying, and Jesus carrying the cross, to invite people to a silent retreat. The retreats are monthly. For women, they are Feb. 21, March 21, etc (every third Saturday), and for men they are Feb. 28, March 28, etc (every fourth Saturday). I want each month date to show for both women and men. Our logo should be in there, which is similar to the Holy family icon attached. Also, show that cost is $80, and the place for the retreats is Casa Alborada, 4187 Juniper Ct, Falls Church, VA and for more information to contact, for women 540-555-0147 and for men 571-555-0182. I will use the flyer for around 4 x 6 or 3 x 5 postcard. Organizers are: Nidos de Valle Claro. The flyer needs to be in spanish "RETIROS EN SILENCIO" and the months should be labeled in Spanish too.

```html
<!DOCTYPE html>
<html lang="es">
<head>
<meta charset="utf-8">
<title>Retiros en Silencio</title>
<link rel="stylesheet" href="https://fonts.googleapis.com/css2?family=Gloock&family=Inter:wght@500&display=swap">
<style>
  :root {
    --red: #d31d3a;
    --red-deep: #8e1426;
    --ink: #231f20;
    --white: #ffffff;
    --gold: #f2a72a;
    --frame: #7d6a3e;
  }
  * { margin: 0; padding: 0; box-sizing: border-box; }
  html, body { width: 1200px; height: 800px; overflow: hidden; background: var(--ink); }
  .flyer {
    position: relative; width: 1200px; height: 800px; overflow: hidden;
    background: var(--ink); color: var(--white);
    font-family: "Inter", Arial, sans-serif; font-weight: 500;
  }
  .main-panel {
    position: absolute; left: 0; top: 0; width: 851px; height: 800px;
    border-radius: 0 92px 88px 0;
    background:
      radial-gradient(ellipse at 60% 40%, rgba(120,10,30,.55), transparent 60%),
      linear-gradient(160deg, var(--red) 0%, #c41934 55%, var(--red-deep) 100%);
  }
  .holy-family-icon { position: absolute; left: 61px; top: 120px; width: 207px; height: 292px; }
  .display { font-family: "Gloock", Georgia, serif; font-weight: 400; }
  .abs { position: absolute; white-space: nowrap; }
  .title { right: 398px; text-align: right; font-size: 80px; line-height: 1; letter-spacing: -2px; }
  .title-1 { top: 44px; }
  .title-2 { top: 132px; }
  .organizer { right: 399px; top: 210px; font-size: 30px; line-height: 1; }
  .intro { right: 399px; text-align: right; font-size: 21px; line-height: 27px; }
  .intro-1 { top: 281px; }
  .intro-2 { top: 361px; }
  .dates-title { left: 57px; top: 446px; font-size: 40px; line-height: 1; }
  .group-label { left: 57px; color: var(--gold); font-size: 21px; line-height: 1; }
  .dates { left: 57px; font-size: 21px; line-height: 27px; }
  .dates .sep { margin: 0 5px; }
  .label-women { top: 503px; }
  .dates-women { top: 525px; }
  .label-men { top: 601px; }
  .dates-men { top: 623px; }
  .closing { left: 57px; top: 709px; font-size: 21px; line-height: 27px; }
  .side-heading { left: 887px; font-size: 40px; line-height: 1; }
  .heading-place { top: 50px; }
  .heading-info { top: 194px; }
  .side-text { left: 887px; font-size: 21.5px; line-height: 27px; }
  .address { top: 87px; }
  .contacts { top: 230px; }
  .contacts .who { color: var(--gold); }
  .cost-label { left: 887px; top: 340px; font-size: 96px; line-height: 1; }
  .cost-amount { left: 884px; top: 452px; font-size: 155px; line-height: 1; letter-spacing: -4px; }
  .footer { left: 887px; top: 682px; font-size: 21.5px; line-height: 27px; }
  .footer .web { color: var(--gold); }
</style>
</head>
<body>
<div class="flyer">
  <div class="main-panel" role="img" aria-label="Pintura en tonos rojos de Jesús cargando la cruz entre la multitud"></div>

  <svg class="holy-family-icon" viewBox="0 0 207 292" role="img" aria-label="Ícono de la Sagrada Familia en marco dorado">
    <defs>
      <linearGradient id="iconFill" x1="0" y1="0" x2="0" y2="1">
        <stop offset="0" stop-color="#c9a25a"/>
        <stop offset="0.5" stop-color="#b23a2a"/>
        <stop offset="1" stop-color="#8a2a1e"/>
      </linearGradient>
    </defs>
    <polygon points="103.5,0 207,48 207,292 0,292 0,48" fill="var(--frame)"/>
    <polygon points="103.5,14 193,56 193,278 14,278 14,56" fill="url(#iconFill)"/>
  </svg>

  <div class="abs display title title-1">RETIROS EN</div>
  <div class="abs display title title-2">SILENCIO</div>
  <div class="abs organizer">Nidos de Valle Claro</div>

  <p class="abs intro intro-1">Ven y encuentra la paz en el silencio<br>con la Virgen María y Jesús.</p>
  <p class="abs intro intro-2">Un día de retiro para renovar tu corazón<br>y fortalecer tu fe.</p>

  <h2 class="abs display dates-title">Fechas de Retiros</h2>
  <div class="abs group-label label-women">Para Mujeres – Cada tercer sábado del mes</div>
  <p class="abs dates dates-women">17 Enero<span class="sep">•</span>21 Febrero<span class="sep">•</span>21 Marzo<span class="sep">•</span>18 Abril<span class="sep">•</span>16 Mayo<span class="sep">•</span>20 Junio<span class="sep">•</span>18 Julio<br>15 Agosto<span class="sep">•</span>19 Septiembre<span class="sep">•</span>17 Octubre<span class="sep">•</span>21 Noviembre<span class="sep">•</span>19 Diciembre</p>
  <div class="abs group-label label-men">Para Hombres – Cada cuarto sábado del mes</div>
  <p class="abs dates dates-men">24 Enero<span class="sep">•</span>28 Febrero<span class="sep">•</span>28 Marzo<span class="sep">•</span>25 Abril<span class="sep">•</span>23 Mayo<span class="sep">•</span>27 Junio<span class="sep">•</span>25 Julio<br>22 Agosto<span class="sep">•</span>26 Septiembre<span class="sep">•</span>24 Octubre<span class="sep">•</span>28 Noviembre<span class="sep">•</span>26 Diciembre</p>

  <p class="abs closing">Con la Virgen María intercediendo y Jesús cargando la cruz, vivamos<br>juntos un encuentro de fe, oración y silencio.</p>

  <h3 class="abs display side-heading heading-place">Lugar:</h3>
  <p class="abs side-text address">Casa Alborada<br>4187 Juniper Ct<br>Falls Church, VA</p>

  <h3 class="abs display side-heading heading-info">Información:</h3>
  <p class="abs side-text contacts"><span class="who">Mujeres:</span> 540-555-0147<br><span class="who">Hombres:</span> 571-555-0182</p>

  <div class="abs display cost-label">Costo:</div>
  <div class="abs display cost-amount">$80</div>

  <p class="abs footer">Nidos de Valle Claro<br><span class="web">nidosdevalleclaro.org</span></p>
</div>
</body>
</html>
```